Brindle 48 Focus Wheel

We need a professional **framework wheel diagram** designed for our detection dog training manual.

Our business is **Brindle 48 Dog Training**, and this graphic represents our **Detection Training Model**.

Please use the **attached reference images** as a guide for the structure and layout of the wheel.

### What we need

1. **Full wheel graphic**

* Clean circular framework wheel
* Similar structure to the attached example
* Clear sections and text
* Professional training manual style
* Transparent background

2. **Individual segment pieces**

We also need the **inner sections broken into separate pieces** (like the second reference image).

This will allow us to place each section on different pages of the manual when explaining the concepts.

Each piece should look like a **slice of the wheel**.

### Style

The design should look:

• Professional
• Clean and modern
• Structured and easy to read
• Suitable for a training manual

Avoid cartoon styles or clipart.

### Colours

Please use our brand colour palette (see attached image):

* Dark navy blue
* Steel blue
* Light blue
* White
* Light grey
* Dark grey

### Files required

Final files must include:

* Vector files (AI or EPS)
* Transparent PNG
* High-resolution PDF

Please also provide **each segment exported individually**

```html
<!DOCTYPE html>
<html lang="en">
<head>
<meta charset="utf-8">
<title>Brindle 48 Focus Wheel</title>
<link rel="stylesheet" href="https://fonts.googleapis.com/css2?family=Montserrat:wght@400;500;600;700&display=swap">
<style>
  :root {
    --navy: #2f4b6b;
    --navy-rim: #3e6189;
    --steel: #5596ae;
    --light-blue: #67a6c1;
    --white: #ffffff;
    --grey: #666666;
    --grey-rim: #4d4d4d;
    --dark-grey: #333333;
    --ink: #111111;
  }
  html, body {
    margin: 0;
    padding: 0;
    width: 1200px;
    height: 435px;
    overflow: hidden;
    background: var(--white);
  }
  .canvas {
    display: block;
    width: 1200px;
    height: 435px;
    font-family: "Montserrat", sans-serif;
  }
  .navy-rim { fill: var(--navy-rim); }
  .navy { fill: var(--navy); }
  .grey-rim { fill: var(--grey-rim); }
  .grey { fill: var(--grey); }
  .steel { fill: var(--steel); }
  .light-blue { fill: var(--light-blue); }

  .piece-label { fill: var(--white); font-weight: 600; font-size: 14px; text-anchor: middle; }
  .ops-piece-label { fill: var(--white); font-weight: 700; font-size: 21px; text-anchor: middle; }
  .group-title { font-weight: 700; font-size: 28px; text-anchor: middle; }
  .group-title--dog { fill: var(--navy); }
  .group-title--ink { fill: var(--ink); }

  .wheel-label { fill: var(--white); font-weight: 600; font-size: 18px; text-anchor: middle; }
  .wheel-inner-label { fill: var(--white); font-weight: 400; font-size: 14px; text-anchor: middle; }
  .sector-line { stroke: var(--white); stroke-width: 2; }
  .sector-line--grey { stroke: #9a9a9a; stroke-width: 2; }
  .ring-text { fill: var(--white); font-weight: 600; font-size: 40px; letter-spacing: 2px; }
  .band-text-dog { fill: var(--navy); font-weight: 600; font-size: 21px; letter-spacing: 1px; }
  .band-text-handler { fill: var(--white); font-weight: 600; font-size: 21px; letter-spacing: 1px; }
  .brand-name { fill: var(--navy); font-weight: 700; font-size: 17px; text-anchor: middle; }
</style>
</head>
<body>
<svg class="canvas" viewBox="0 0 2560 928" xmlns="http://www.w3.org/2000/svg" role="img" aria-label="Brindle 48 Focus Wheel: dog and handler foundations, full wheel, and operational capability area pieces">
  <defs>
    <path id="dog-piece-rim" d="M0 0 L-58.7 -180.7 A190 190 0 0 1 58.7 -180.7 Z"/>
    <path id="dog-piece-core" d="M0 0 L-52.5 -161.7 A170 170 0 0 1 52.5 -161.7 Z"/>
    <path id="handler-piece-rim" d="M0 0 L-72.7 -175.5 A190 190 0 0 1 72.7 -175.5 Z"/>
    <path id="handler-piece-core" d="M0 0 L-65.1 -157.1 A170 170 0 0 1 65.1 -157.1 Z"/>
    <path id="ops-top-rim" d="M0 0 L-94.3 -290.1 A305 305 0 0 1 94.3 -290.1 Z"/>
    <path id="ops-top-core" d="M0 0 L-87.5 -269.1 A283 283 0 0 1 87.5 -269.1 Z"/>
    <path id="ops-bottom-rim" d="M0 0 L-116.7 -281.8 A305 305 0 0 1 116.7 -281.8 Z"/>
    <path id="ops-bottom-core" d="M0 0 L-108.3 -261.5 A283 283 0 0 1 108.3 -261.5 Z"/>

    <path id="ring-top-path" d="M867 462 A340 340 0 0 1 1547 462"/>
    <path id="ring-bottom-path" d="M839 462 A368 368 0 0 0 1575 462"/>
    <path id="band-dog-path" d="M1015 462 A192 192 0 0 1 1399 462"/>
    <path id="band-handler-path" d="M996 462 A211 211 0 0 0 1418 462"/>
  </defs>

  <!-- Dog foundations pieces -->
  <g class="dog-foundations">
    <g transform="translate(343 426) rotate(-72)"><use href="#dog-piece-rim" class="navy-rim"/><use href="#dog-piece-core" class="navy"/></g>
    <g transform="translate(366 395) rotate(-36)"><use href="#dog-piece-rim" class="navy-rim"/><use href="#dog-piece-core" class="navy"/></g>
    <g transform="translate(402 383)"><use href="#dog-piece-rim" class="navy-rim"/><use href="#dog-piece-core" class="navy"/></g>
    <g transform="translate(438 395) rotate(36)"><use href="#dog-piece-rim" class="navy-rim"/><use href="#dog-piece-core" class="navy"/></g>
    <g transform="translate(461 426) rotate(72)"><use href="#dog-piece-rim" class="navy-rim"/><use href="#dog-piece-core" class="navy"/></g>

    <text class="piece-label" x="221" y="383">Arousal<tspan x="221" dy="15">Regulation</tspan></text>
    <text class="piece-label" x="288" y="284">Genetic<tspan x="288" dy="15">Suitability</tspan></text>
    <text class="piece-label" x="402" y="233">Health &amp;<tspan x="402" dy="15">Physical</tspan><tspan x="402" dy="15">Wellbeing</tspan></text>
    <text class="piece-label" x="516" y="284">Reward<tspan x="516" dy="15">Value</tspan></text>
    <text class="piece-label" x="583" y="383">Engagement<tspan x="583" dy="15">Relationship</tspan></text>

    <text class="group-title group-title--dog" x="408" y="488">Dog Foundations</text>
  </g>

  <!-- Handler foundations pieces -->
  <g class="handler-foundations">
    <g transform="translate(465 548) rotate(112.5)"><use href="#handler-piece-rim" class="grey-rim"/><use href="#handler-piece-core" class="grey"/></g>
    <g transform="translate(433 590) rotate(157.5)"><use href="#handler-piece-rim" class="grey-rim"/><use href="#handler-piece-core" class="grey"/></g>
    <g transform="translate(387 590) rotate(202.5)"><use href="#handler-piece-rim" class="grey-rim"/><use href="#handler-piece-core" class="grey"/></g>
    <g transform="translate(355 548) rotate(247.5)"><use href="#handler-piece-rim" class="grey-rim"/><use href="#handler-piece-core" class="grey"/></g>

    <text class="piece-label" x="246" y="599">Dog Safety</text>
    <text class="piece-label" x="574" y="599">Read the Dog</text>
    <text class="piece-label" x="343" y="694">Search<tspan x="343" dy="15">Coverage</tspan></text>
    <text class="piece-label" x="481" y="695">Minimal<tspan x="481" dy="15">Necessary</tspan><tspan x="481" dy="15">Involvement</tspan></text>

    <text class="group-title group-title--ink" x="408" y="828">Handler Foundations</text>
  </g>

  <!-- Full wheel -->
  <g class="full-wheel">
    <circle cx="1207" cy="462" r="375" class="light-blue"/>
    <circle cx="1207" cy="462" r="332" class="navy"/>

    <g class="outer-sector-lines">
      <line class="sector-line" x1="1273.4" y1="257.5" x2="1309.6" y2="146.3"/>
      <line class="sector-line" x1="1140.6" y1="257.5" x2="1104.4" y2="146.3"/>
      <line class="sector-line" x1="1380.9" y1="335.6" x2="1475.6" y2="266.8"/>
      <line class="sector-line" x1="1033.1" y1="335.6" x2="938.4" y2="266.8"/>
      <line class="sector-line" x1="1422" y1="462" x2="1539" y2="462"/>
      <line class="sector-line" x1="992" y1="462" x2="875" y2="462"/>
      <line class="sector-line" x1="1359" y1="614" x2="1441.7" y2="696.7"/>
      <line class="sector-line" x1="1055" y1="614" x2="972.3" y2="696.7"/>
      <line class="sector-line" x1="1207" y1="677" x2="1207" y2="794"/>
    </g>

    <circle cx="1207" cy="462" r="215" fill="var(--white)"/>
    <path d="M992 462 A215 215 0 0 0 1422 462 Z" fill="var(--dark-grey)"/>
    <path d="M1019 462 A188 188 0 0 1 1395 462 Z" class="light-blue"/>
    <path d="M1395 462 A188 188 0 0 1 1019 462 Z" class="grey"/>

    <g class="inner-sector-lines">
      <line class="sector-line" x1="1226.2" y1="403" x2="1265.1" y2="283.2"/>
      <line class="sector-line" x1="1187.8" y1="403" x2="1148.9" y2="283.2"/>
      <line class="sector-line" x1="1257.2" y1="425.5" x2="1359.1" y2="351.5"/>
      <line class="sector-line" x1="1156.8" y1="425.5" x2="1054.9" y2="351.5"/>
      <line class="sector-line--grey" x1="1250.8" y1="505.8" x2="1339.9" y2="594.9"/>
      <line class="sector-line--grey" x1="1163.2" y1="505.8" x2="1074.1" y2="594.9"/>
      <line class="sector-line--grey" x1="1207" y1="524" x2="1207" y2="650"/>
    </g>

    <text class="ring-text"><textPath href="#ring-top-path" startOffset="50%" text-anchor="middle">OPERATIONAL CAPABILITY AREA</textPath></text>
    <text class="ring-text"><textPath href="#ring-bottom-path" startOffset="50%" text-anchor="middle">OPERATIONAL CAPABILITY AREA</textPath></text>
    <text class="band-text-dog"><textPath href="#band-dog-path" startOffset="50%" text-anchor="middle">DOG FOUNDATIONS</textPath></text>
    <text class="band-text-handler"><textPath href="#band-handler-path" startOffset="50%" text-anchor="middle">HANDLER FOUNDATIONS</textPath></text>

    <text class="wheel-label" x="1204" y="205">Distractions</text>
    <text class="wheel-label" x="1039" y="259">Development</text>
    <text class="wheel-label" x="1374" y="259">Behaviour</text>
    <text class="wheel-label" x="943" y="394">Integrity</text>
    <text class="wheel-label" x="1470" y="394">Handler</text>
    <text class="wheel-label" x="951" y="548">Target<tspan x="951" dy="23">Odour</tspan></text>
    <text class="wheel-label" x="1460" y="548">Search<tspan x="1460" dy="23">Method</tspan></text>
    <text class="wheel-label" x="1096" y="713">Deployment</text>
    <text class="wheel-label" x="1307" y="713">Reinforcement</text>

    <text class="wheel-inner-label" x="1207" y="313">Health &amp;<tspan x="1207" dy="16">Physical</tspan><tspan x="1207" dy="16">Wellbeing</tspan></text>
    <text class="wheel-inner-label" x="1124" y="353">Genetic<tspan x="1124" dy="16">Suitability</tspan></text>
    <text class="wheel-inner-label" x="1291" y="353">Reward<tspan x="1291" dy="16">Value</tspan></text>
    <text class="wheel-inner-label" x="1078" y="424">Arousal<tspan x="1078" dy="16">Regulation</tspan></text>
    <text class="wheel-inner-label" x="1330" y="428">Engagement<tspan x="1330" dy="16">Relationship</tspan></text>
    <text class="wheel-inner-label" x="1087" y="507">Dog Safety</text>
    <text class="wheel-inner-label" x="1318" y="507">Read the Dog</text>
    <text class="wheel-inner-label" x="1156" y="570">Search<tspan x="1156" dy="16">Coverage</tspan></text>
    <text class="wheel-inner-label" x="1262" y="565">Minimal<tspan x="1262" dy="16">Necessary</tspan><tspan x="1262" dy="16">Involvement</tspan></text>

    <g class="brand-hub">
      <circle cx="1207" cy="462" r="62" class="navy"/>
      <circle cx="1207" cy="462" r="46" fill="var(--white)"/>
      <text class="brand-name" x="1207" y="468">Brindle 48</text>
    </g>
  </g>

  <!-- Operational capabilities area pieces -->
  <g class="operational-capabilities">
    <g transform="translate(1985 420) rotate(-72)"><use href="#ops-top-rim" class="steel"/><use href="#ops-top-core" class="light-blue"/></g>
    <g transform="translate(2010 355) rotate(-36)"><use href="#ops-top-rim" class="steel"/><use href="#ops-top-core" class="light-blue"/></g>
    <g transform="translate(2077 398)"><use href="#ops-top-rim" class="steel"/><use href="#ops-top-core" class="light-blue"/></g>
    <g transform="translate(2142 365) rotate(36)"><use href="#ops-top-rim" class="steel"/><use href="#ops-top-core" class="light-blue"/></g>
    <g transform="translate(2130 425) rotate(72)"><use href="#ops-top-rim" class="steel"/><use href="#ops-top-core" class="light-blue"/></g>

    <g transform="translate(2117 472) rotate(112.5)"><use href="#ops-bottom-rim" class="steel"/><use href="#ops-bottom-core" class="light-blue"/></g>
    <g transform="translate(2117 535) rotate(157.5)"><use href="#ops-bottom-rim" class="steel"/><use href="#ops-bottom-core" class="light-blue"/></g>
    <g transform="translate(2015 548) rotate(202.5)"><use href="#ops-bottom-rim" class="steel"/><use href="#ops-bottom-core" class="light-blue"/></g>
    <g transform="translate(2017 465) rotate(247.5)"><use href="#ops-bottom-rim" class="steel"/><use href="#ops-bottom-core" class="light-blue"/></g>

    <text class="ops-piece-label" x="1873" y="197">Development</text>
    <text class="ops-piece-label" x="2077" y="184">Distractions</text>
    <text class="ops-piece-label" x="2276" y="214">Behaviour</text>
    <text class="ops-piece-label" x="1804" y="374">Integrity</text>
    <text class="ops-piece-label" x="2320" y="380">Handler</text>
    <text class="ops-piece-label" x="1840" y="531">Target Odour</text>
    <text class="ops-piece-label" x="2299" y="537">Search Method</text>
    <text class="ops-piece-label" x="1927" y="737">Deployment</text>
    <text class="ops-piece-label" x="2207" y="724">Reinforcement</text>

    <text class="group-title group-title--ink" x="2062" y="894">Operational Capabilities Area</text>
  </g>
</svg>
</body>
</html>
```